Bref créative
Business Card for Business Advisory Firm
Marlowe Partners
Simple
Tom Brackett
Solutions Strategist
47 Pellham Road
Suite K
Boston, MA 02184
tbrackett@marlowepartners.example
www.marlowepartners.example
Somewhere on the front of the card I would like to list some of the services of the firm:
Project Support
Operations Analysis
Business Development
Would like a blue gingham pattern on entire back using the same colors as in the logo.
Layout guidelines: I will be using Zeb to print the cards. If there are any questions about layout for bleed etc, they can be found at link below:
http://us.zebprint.example/help/faq/templates-and-guidelines.html
Final, trimmed size
3.30" x 2.16"
84mm x 55mm
Full bleed size (recommended for creating finished artwork)
1039 x 697 pixels (300dpi)
3.46" x 2.32" (300dpi)
88mm x 59mm (300dpi)

```html
<!DOCTYPE html>
<html lang="en">
<head>
<meta charset="utf-8">
<title>Marlowe Partners – Business Card</title>
<link href="https://fonts.googleapis.com/css2?family=Open+Sans:wght@400;600;700&display=swap" rel="stylesheet">
<style>
  :root {
    --page-bg: #e9e7e3;
    --card-white: #ffffff;
    --brand-blue: #2f45ad;
    --brand-blue-deep: #1f2f86;
    --brand-blue-light: #4a5fc4;
    --ink-dark: #333a44;
    --ink-white: #ffffff;
  }
  * { box-sizing: border-box; margin: 0; padding: 0; }
  html, body {
    width: 1200px; height: 900px; overflow: hidden;
    background: var(--page-bg);
    font-family: "Open Sans", Arial, sans-serif;
  }
  .card {
    position: absolute; left: 120px; top: 136px;
    width: 960px; height: 628px;
    background: var(--card-white);
    box-shadow: 0 6px 24px rgba(0,0,0,0.18);
    overflow: hidden;
  }
  .card__band {
    position: absolute; left: 0; right: 0; top: 272px; bottom: 0;
    background: linear-gradient(180deg, var(--brand-blue-light) 0%, var(--brand-blue) 12%, var(--brand-blue) 55%, var(--brand-blue-deep) 100%);
  }
  .card__band::before {
    content: ""; position: absolute; left: 0; right: 0; top: 0; height: 6px;
    background: var(--brand-blue-light);
  }
  .services {
    position: absolute; right: 44px; top: 40px;
    text-align: right; color: var(--ink-dark);
    font-size: 27px; line-height: 32px; font-weight: 400;
    list-style: none;
  }
  .brand {
    position: absolute; left: 40px; top: 150px;
    display: flex; align-items: center; gap: 22px;
  }
  .brand__square {
    width: 84px; height: 84px; background: var(--brand-blue);
    transform: rotate(45deg);
    margin: 0 8px;
  }
  .brand__name {
    font-size: 46px; font-weight: 700; color: var(--brand-blue);
    line-height: 1;
  }
  .person {
    position: absolute; right: 44px; top: 372px;
    text-align: right; color: var(--ink-white);
  }
  .person__name { font-size: 28px; font-weight: 700; line-height: 36px; }
  .person__title { font-size: 24px; font-weight: 400; line-height: 32px; }
  .contact {
    position: absolute; left: 28px; top: 432px;
    list-style: none; color: var(--ink-white);
    font-size: 15px; line-height: 20px;
  }
  .contact__item { display: flex; align-items: flex-start; gap: 8px; margin-bottom: 5px; }
  .contact__icon {
    flex: 0 0 18px; width: 18px; height: 18px; margin-top: 1px;
  }
</style>
</head>
<body>
  <main class="card">
    <div class="card__band"></div>

    <ul class="services">
      <li>Project Support</li>
      <li>Operations Analysis</li>
      <li>Business Development</li>
    </ul>

    <div class="brand">
      <span class="brand__square" aria-hidden="true"></span>
      <span class="brand__name">Marlowe Partners</span>
    </div>

    <div class="person">
      <p class="person__name">Tom Brackett</p>
      <p class="person__title">Solutions Strategist</p>
    </div>

    <ul class="contact">
      <li class="contact__item">
        <svg class="contact__icon" viewBox="0 0 18 18" aria-hidden="true"><circle cx="9" cy="9" r="9" fill="#fff"/><path d="M4.5 9.2 9 5.2l4.5 4h-1.3v3.6H10V10.4H8v2.4H5.8V9.2z" fill="#2f45ad"/></svg>
        <span>47 Pellham Road Suite K<br>Boston, MA 02184</span>
      </li>
      <li class="contact__item">
        <svg class="contact__icon" viewBox="0 0 18 18" aria-hidden="true"><circle cx="9" cy="9" r="9" fill="#fff"/><path d="M6 4.5c.6 0 1.4 1.6 1.4 2.1 0 .6-.8.8-.8 1.3 0 .8 1.7 2.6 2.6 2.6.5 0 .7-.8 1.3-.8.5 0 2.1.8 2.1 1.4 0 .9-1.2 1.8-2 1.8-2.4 0-6.3-3.8-6.3-6.3 0-.8.9-2.1 1.7-2.1z" fill="#2f45ad"/></svg>
        <span>617-555-0142</span>
      </li>
      <li class="contact__item">
        <svg class="contact__icon" viewBox="0 0 18 18" aria-hidden="true"><circle cx="9" cy="9" r="9" fill="#fff"/><rect x="5" y="6" width="8" height="7" rx="1" fill="#2f45ad"/><rect x="6.5" y="4" width="5" height="3" fill="#2f45ad"/></svg>
        <span>508-555-0187</span>
      </li>
      <li class="contact__item">
        <svg class="contact__icon" viewBox="0 0 18 18" aria-hidden="true"><circle cx="9" cy="9" r="9" fill="#fff"/><rect x="4.5" y="5.5" width="9" height="7" fill="#2f45ad"/><path d="M4.8 6 9 9.4 13.2 6" stroke="#fff" stroke-width="1" fill="none"/></svg>
        <span>tbrackett@marlowepartners.example</span>
      </li>
      <li class="contact__item">
        <svg class="contact__icon" viewBox="0 0 18 18" aria-hidden="true"><circle cx="9" cy="9" r="9" fill="#fff"/><circle cx="9" cy="9" r="4.8" fill="none" stroke="#2f45ad" stroke-width="1.2"/><path d="M4.2 9h9.6M9 4.2c-2 2.6-2 7 0 9.6M9 4.2c2 2.6 2 7 0 9.6" stroke="#2f45ad" stroke-width="1" fill="none"/></svg>
        <span>www.marlowepartners.example</span>
      </li>
    </ul>
  </main>
</body>
</html>
```